New Business Card Design Project

We are looking for a talented individual to create a truly awesome/unique business card design for us. We are looking for a someone to design something that will really stand out from the crowd - we don't mind what ideas you come up with (ie embossed/flat/matte/shine etc etc) just wow us with your creativity.
Updates

Target Market(s)

Video Games Industry Professionals (all levels of seniority from QA Testers through to CEOs)

Contact Information for Business Card

Company logo (see upload)
Company name: Northbay Play Careers Ltd
Employee Name: Darren Elsby
Job title: CEO
Website: www.nbpc2go.example
Office +44 1632 960418
Mobile: +44 7700 900276
Email: darren@nbpc2go.example

Colors

Designer to choose colors to be used in the design.

Requirements
Must have
• The business card design MUST contain all the information listed in the BUSINESS CARD DETAILS box.
• You will see the colours that are relevant to us (ie company logo) in the uploaded imagery - however you do not have to use all these colours when designing the business card itself
• MUST BE DOUBLE SIDED

```html
<!DOCTYPE html>
<html lang="en">
<head>
<meta charset="utf-8">
<title>Northbay Play Careers – Business Card</title>
<link rel="stylesheet" href="https://fonts.googleapis.com/css2?family=Exo+2:wght@700;800&family=Arimo:wght@400;700&display=swap">
<style>
  :root {
    --navy: #1f2f63;
    --navy-deep: #172452;
    --orange: #f07a1e;
    --paper: #ffffff;
    --ghost: #dfe1ec;
    --ink: #2a2a2a;
    --stage: #ecebe8;
  }
  * { box-sizing: border-box; margin: 0; padding: 0; }
  html, body { width: 1200px; height: 900px; overflow: hidden; }
  body { background: var(--stage); position: relative; font-family: "Arimo", Arial, sans-serif; }

  .card {
    position: absolute;
    left: 240px;
    width: 720px;
    height: 412px;
    overflow: hidden;
    box-shadow: 0 6px 18px rgba(0,0,0,.18);
  }
  .card--front { top: 28px; background: var(--navy); }
  .card--back { top: 460px; background: var(--paper); }

  /* Front */
  .front-brand { position: absolute; left: 44px; top: 150px; color: var(--paper); }
  .wordmark {
    font-family: "Exo 2", Arial, sans-serif;
    font-weight: 800;
    font-size: 40px;
    line-height: 1.02;
    letter-spacing: .5px;
  }
  .front-brand .wordmark { color: var(--paper); }
  .legal-name {
    margin-top: 10px;
    font-family: "Exo 2", Arial, sans-serif;
    font-weight: 700;
    font-size: 16px;
    letter-spacing: 1px;
  }
  .front-art {
    position: absolute;
    right: 30px; top: 40px;
    width: 340px; height: 330px;
    border-radius: 48% 40% 44% 50%;
    background: radial-gradient(ellipse at 55% 50%, #f3f4f8 0%, #c9cde0 55%, rgba(31,47,99,0) 75%);
  }

  /* Back */
  .back-brand { position: absolute; left: 44px; top: 34px; }
  .back-brand .wordmark { color: var(--navy); font-size: 44px; }
  .back-art {
    position: absolute;
    right: 40px; top: 110px;
    width: 330px; height: 280px;
    border-radius: 48% 40% 44% 50%;
    background: radial-gradient(ellipse at 55% 50%, var(--ghost) 0%, #e9eaf2 55%, rgba(255,255,255,0) 75%);
  }
  .person { position: absolute; left: 44px; top: 168px; }
  .person-name {
    font-family: "Exo 2", Arial, sans-serif;
    font-weight: 800;
    font-size: 30px;
    color: var(--navy);
    line-height: 1;
  }
  .person-title {
    font-family: "Exo 2", Arial, sans-serif;
    font-weight: 700;
    font-size: 16px;
    color: var(--orange);
    margin-top: 4px;
  }
  .phones { margin-top: 10px; font-size: 14px; color: var(--ink); line-height: 1.45; }
  .label { font-weight: 700; margin-right: 6px; }

  .rule { position: absolute; left: 0; top: 0; width: 720px; height: 412px; }

  .online {
    position: absolute;
    right: 44px; bottom: 40px;
    font-size: 14px; color: var(--ink); line-height: 1.45;
  }
</style>
</head>
<body>

<section class="card card--front" aria-label="Card front">
  <div class="front-brand">
    <div class="wordmark">Northbay Play<br>Careers</div>
    <div class="legal-name">Northbay Play Careers Ltd</div>
  </div>
  <div class="front-art" role="img" aria-label="Illustration of a horned-helmet warrior head with flowing hair"></div>
</section>

<section class="card card--back" aria-label="Card back">
  <div class="back-art" role="img" aria-label="Faint large warrior head illustration used as background decoration"></div>

  <svg class="rule" viewBox="0 0 720 412" aria-hidden="true">
    <line x1="44" y1="300" x2="640" y2="300" stroke="var(--orange)" stroke-width="2"/>
    <polygon points="0,372 380,372 350,412 0,412" fill="var(--orange)"/>
    <polygon points="0,380 374,380 346,412 0,412" fill="var(--navy)"/>
  </svg>

  <div class="back-brand">
    <div class="wordmark">Northbay Play Careers</div>
  </div>

  <div class="person">
    <div class="person-name">Darren Elsby</div>
    <div class="person-title">CEO</div>
    <div class="phones">
      <div><span class="label">Mobile:</span>+44 7700 900276</div>
      <div><span class="label">Office:</span>+44 1632 960418</div>
    </div>
  </div>

  <div class="online">
    <div><span class="label">Email:</span>darren@nbpc2go.example</div>
    <div><span class="label">Web:</span>www.nbpc2go.example</div>
  </div>
</section>

</body>
</html>
```